Corporate Design für Softwareentwickler
Schon das erste Design hat mir sehr gut gefallen. Einige kleinere Anpassungen, die ich gerne haben wollte, wurden sehr schnell in den Entwurf aufgenommen und sehr gut umgesetzt. Insgesamt bin ich mit dem Ablauf des Projekts und dem entstanden Ergebnis sehr zufrieden. Jederzeit gerne wieder...
Zielgruppe
Wir erstellen individuelle Software nach Kundenvorgabe. Schwerpunkt dabei sind Web-Anwendungen. Die Zielgruppe sind ausschließlich Firmenkunden.
Aufgabenstellung
Ich hätte gerne ein einfaches, klares und modernes Design. Es sollte Kompetenz und Zuverlässigkeit ausstrahlen.

```html
<!DOCTYPE html>
<html lang="en">
<head>
<meta charset="utf-8">
<title>kruvo – Corporate Stationery</title>
<link rel="stylesheet" href="https://fonts.googleapis.com/css2?family=Open+Sans:wght@400;600;700&display=swap">
<style>
  :root {
    --brand-blue: #0a2fa8;
    --paper: #ffffff;
    --backdrop: #e8eaed;
    --ink: #2a3550;
    --window: #ececec;
    --shadow: 0 6px 18px rgba(20, 30, 60, 0.14);
  }
  * { margin: 0; padding: 0; box-sizing: border-box; }
  html, body {
    width: 1200px; height: 900px; overflow: hidden;
    background: var(--backdrop);
    font-family: "Open Sans", Arial, sans-serif;
    color: var(--ink);
  }
  .stationery { position: relative; width: 1200px; height: 900px; }
  .sheet {
    position: absolute; overflow: hidden;
    background: var(--paper); box-shadow: var(--shadow);
  }

  /* logo lockup */
  .brand { display: flex; align-items: center; gap: 8px; color: var(--brand-blue); }
  .brand__mark { width: 28px; height: 28px; background: var(--brand-blue); flex: none; }
  .brand__text { display: flex; flex-direction: column; line-height: 1; }
  .brand__tagline { font-size: 6.5px; font-weight: 600; letter-spacing: 0.12em; margin-bottom: 2px; }
  .brand__name { font-size: 30px; font-weight: 700; letter-spacing: -0.01em; }
  .brand--light { color: var(--paper); }
  .brand--light .brand__mark { background: var(--paper); }

  .corner-square {
    position: absolute; background: var(--brand-blue);
  }

  /* letterhead */
  .letterhead { left: 420px; top: 36px; width: 430px; height: 608px; }
  .letterhead .brand { position: absolute; top: 40px; right: 36px; }
  .letter { position: absolute; left: 40px; top: 40px; width: 300px; font-size: 7.5px; line-height: 1.55; }
  .letter__address { margin-bottom: 14px; }
  .letter__date { margin-bottom: 22px; }
  .letter p { margin-bottom: 9px; }
  .letterhead .corner-square { width: 170px; height: 170px; right: 28px; bottom: -40px; }

  /* folder */
  .folder { left: 885px; top: 110px; width: 285px; height: 420px; background: var(--brand-blue); }
  .folder .brand { position: absolute; top: 40px; left: 28px; }

  /* envelope */
  .envelope { left: 380px; top: 672px; width: 440px; height: 208px; }
  .envelope .brand { position: absolute; top: 24px; left: 28px; }
  .envelope__window {
    position: absolute; left: 28px; top: 96px; width: 160px; height: 68px;
    background: var(--window); border-radius: 8px;
  }
  .envelope .corner-square { width: 120px; height: 120px; right: 26px; bottom: -30px; }

  /* business cards */
  .card { width: 270px; height: 160px; }
  .card--front { left: 70px; top: 230px; background: var(--brand-blue); }
  .card--front .brand { position: absolute; left: 50%; top: 50%; transform: translate(-50%, -50%); }
  .card--back { left: 70px; top: 430px; }
  .card--back .brand { position: absolute; left: 22px; top: 20px; }
  .card--back .brand__name { font-size: 24px; }
  .card--back .brand__mark { width: 22px; height: 22px; }
  .contact { position: absolute; left: 22px; top: 72px; font-size: 8px; line-height: 1.55; }
  .contact__name { font-size: 11px; font-weight: 700; color: var(--brand-blue); }
  .contact__role { margin-bottom: 6px; }
  .card--back .corner-square { width: 70px; height: 70px; right: 18px; bottom: -16px; }
</style>
</head>
<body>
<main class="stationery">

  <section class="sheet card card--front" aria-label="Business card front">
    <div class="brand brand--light">
      <span class="brand__mark"></span>
      <span class="brand__text"><span class="brand__tagline">SOFTWARE DEVELOPMENT</span><span class="brand__name">kruvo</span></span>
    </div>
  </section>

  <section class="sheet card card--back" aria-label="Business card back">
    <div class="brand">
      <span class="brand__mark"></span>
      <span class="brand__text"><span class="brand__tagline">SOFTWARE DEVELOPMENT</span><span class="brand__name">kruvo</span></span>
    </div>
    <div class="contact">
      <div class="contact__name">Yourname</div>
      <div class="contact__role">Software Developer</div>
      <div>T 0123 456 789</div>
      <div>info@kruvo.de</div>
      <div>www.kruvo.de</div>
    </div>
    <span class="corner-square"></span>
  </section>

  <section class="sheet letterhead" aria-label="Letterhead">
    <div class="brand">
      <span class="brand__mark"></span>
      <span class="brand__text"><span class="brand__tagline">SOFTWARE DEVELOPMENT</span><span class="brand__name">kruvo</span></span>
    </div>
    <div class="letter">
      <div class="letter__address">Recipient Name<br>Street Address<br>City, ST ZIP Code</div>
      <div class="letter__date">Date</div>
      <p>Dear Recipient Name,</p>
      <p>Thank you for your interest in our services. We build custom web applications for business clients and would be glad to discuss your next project with you. Please find our proposal enclosed and let us know a suitable date for a first meeting.</p>
      <p>Kind regards and best wishes from the whole team.</p>
      <p>Sincerely,</p>
      <p>Your Name</p>
    </div>
    <span class="corner-square"></span>
  </section>

  <section class="sheet folder" aria-label="Presentation folder">
    <div class="brand brand--light">
      <span class="brand__mark"></span>
      <span class="brand__text"><span class="brand__tagline">SOFTWARE DEVELOPMENT</span><span class="brand__name">kruvo</span></span>
    </div>
  </section>

  <section class="sheet envelope" aria-label="Envelope">
    <div class="brand">
      <span class="brand__mark"></span>
      <span class="brand__text"><span class="brand__tagline">SOFTWARE DEVELOPMENT</span><span class="brand__name">kruvo</span></span>
    </div>
    <div class="envelope__window"></div>
    <span class="corner-square"></span>
  </section>

</main>
</body>
</html>
```